BRAVO Tea & Herbal Tea Packaging Labels

We are seeking new consistent front label designs that we can use for both retail and wholesale packaging purposes:

BRAVO PHILOSOPHY

BRAVO provides a selection of ‘energy enhanced’ signature infusion blends that taste great while assisting a person deeply on several levels – emotional, mental, physical and spiritual.

We source quality ingredients and specifically use certified organic, spray free and wildcrafted ingredients for our herbal blends.

BRAVO’s PRODUCT RANGE

A. 6 standard signature herbal blends (standard range)
B. 2 seasonal blends - which change every quarter (1 x herbal blend, 1 x tea-based blend)
C. selection of teas – black, green, white, oolong (which vary in type and number)
D. custom and limited edition blends – herbal and teas
E. tea drinking accessories.

11 LABELS ARE REQUIRED

Labels 1-8 for Herbal Blends (to be denoted by an accent of SILVER)
Labels 9-10 for Teas (to be denoted by an accent of GOLD)
Label 11 for Accessories

LABEL SIZE

Current front label dimensions: 63.5 x 72mm long – willing to look at alternate label size
Current ‘usable area’ of smallest resealable bag: 110 x 130mm long

** PLEASE SEE ATTACHED WORD DOC FOR COMPLETE SPECIFICATION - PLEASE READ BEFORE COMMENCING ANY WORK **
Updates

hi,

forgot to include an attachment of the current labels for herbal teas that are used... here is a link to the PDF.

http://files.quorvanshare.com/u/48213675/BRAVO-Herbal-Labels.pdf

thanks Derek

Hi,

please note we have attached a jpg of the packaging the label goes onto... it is in the attached files in the brief - called packaging.

thanks Derek

Hi, we've uploaded some pics of the current packaging to give you a sense of the packaging we are using and the space on the front pack to work with.

many thanks.

Target Market(s)

Women and men aged 30-55 with an interest in natural products, emotional/spiritual wellbeing and support.

BRAVO DISTRIBUTION

Online store for retail sales,
Cafes for food service,
Practitioner (naturopaths, massage therapists, energy healers) clinics and stores.

Industry/Entity Type

Retail

Requirements
Must have
• Each label should have:
• Current logo and tagline;
• Website name;
• Silver accent for herbal range labels;
• Gold accent for tea range labels;
• Colour-coding for the 6 signature herbals.
• ** PLEASE SEE ATTACHED WORD DOC FOR COMPLETE SPECIFICATION - PLEASE READ BEFORE COMMENCING ANY WORK **
Nice to have
• Mrs Eaves font for text (to match logo font type)

```html
<!DOCTYPE html>
<html lang="en">
<head>
<meta charset="utf-8">
<title>Mint Haven – Herbal Label</title>
<link href="https://fonts.googleapis.com/css2?family=Questrial&family=Arimo&display=swap" rel="stylesheet">
<style>
  :root {
    --page: #ffffff;
    --label-fill: #b6dcc8;
    --label-border: #3f7a70;
    --rule: #ffffff;
    --ink: #1a1a1a;
    --title: #5e8a84;
    --subtle: #6a8f89;
    --art-tone: #f2f2f2;
  }
  html, body {
    margin: 0;
    padding: 0;
    width: 1062px;
    height: 1200px;
    overflow: hidden;
    background: var(--page);
  }
  .canvas {
    position: relative;
    width: 1062px;
    height: 1200px;
  }
  .label {
    position: absolute;
    left: 66px;
    top: 64px;
    width: 881px;
    height: 1044px;
    background: var(--label-fill);
    border: 11px solid var(--label-border);
    border-radius: 40px;
    box-shadow: 6px 10px 28px rgba(0, 0, 0, 0.35);
  }
  .label > * { position: absolute; margin: 0; }
  .logo-box {
    left: 131px; top: 63px;
    width: 490px; height: 58px;
    border: 1px solid #555;
    display: flex; align-items: center; justify-content: center;
    font-family: "Arimo", sans-serif;
    font-size: 45px; color: var(--ink);
  }
  .tagline {
    left: 131px; width: 530px; top: 148px;
    text-align: center;
    font-family: "Arimo", sans-serif;
    font-size: 37px; color: var(--ink);
  }
  .cup-art {
    left: 686px; top: 21px;
    width: 162px; height: 155px;
    background: linear-gradient(160deg, #ffffff, var(--art-tone));
  }
  .rule {
    left: 29px; top: 216px;
    width: 834px; height: 7px;
    background: var(--rule);
  }
  .product-name {
    left: 163px; top: 268px;
    font-family: "Questrial", sans-serif;
    font-size: 72px; font-weight: 400;
    letter-spacing: 25px;
    color: var(--title); line-height: 1;
    white-space: nowrap;
  }
  .benefits, .certified, .serving-label, .body-copy, .serving-copy {
    font-family: "Questrial", sans-serif;
    font-variant: small-caps;
    white-space: nowrap;
  }
  .benefits {
    left: 36px; top: 367px;
    font-size: 31px; letter-spacing: 6.7px;
    color: var(--subtle);
  }
  .body-copy {
    left: 83px; top: 432px;
    font-size: 33px; letter-spacing: 7.2px;
    line-height: 42.2px; color: var(--ink);
  }
  .certified {
    left: 33px; top: 739px;
    font-size: 42px; letter-spacing: 8.7px;
    color: var(--subtle);
  }
  .serving-label {
    left: 25px; top: 830px;
    font-size: 33px; letter-spacing: 7.7px;
    color: var(--subtle); line-height: 44.7px;
  }
  .serving-copy {
    left: 234px; top: 830px;
    font-size: 33px; letter-spacing: 8.4px;
    line-height: 44.7px; color: var(--ink);
  }
</style>
</head>
<body>
<main class="canvas">
  <section class="label">
    <div class="logo-box">LOGO</div>
    <p class="tagline">“Love in every cup”</p>
    <div class="cup-art" role="img" aria-label="Line illustration of a teacup with two daisies rising from it"></div>
    <div class="rule"></div>
    <h1 class="product-name">MINT HAVEN</h1>
    <p class="benefits">Refreshes, Clarifies, Internal body hug</p>
    <p class="body-copy">for those who love a refreshing<br>mint taste, the gentle flavour of<br>spermint combined with lavender,<br>rose petals &amp; echinacea delight<br>the senses &amp; give what we regard<br>as an “internal body hug”.</p>
    <p class="certified">Certified Organic Ingredients</p>
    <p class="serving-label">Serving:</p>
    <p class="serving-copy">For optimum flavour pour<br>freshly boiled water over<br>one generous teaspoon<br>per cup &amp; steep 3-5 mins.</p>
  </section>
</main>
</body>
</html>
```